Tending Our Garden eBook Cover Design

I want to deisgn a cover for my eBook (FRONT COVER) and the title is:

What I Grew From a Single Spark. And Why It Matters
By KT Dorran

TITLE CHANGED TO: UNDER THE WILLOW TREE; WHERE I FOUND MY QUIET STRENGTH AND WHERE YOU MIGHT TOO

The color palette is attached. Along with some photos options of me. Along with the ebook in WORD Document. My website is www.KTDorranLive.example. You can use a different color palette if you think it is best

Target Market(s)

women who look to build a personal brand

Industry/Entity Type

health and wellness

Requirements
Must have
• the title
Nice to have
• use my picture on the cover; but that is optional
Should not have
• any men

```html
<!DOCTYPE html>
<html lang="en">
<head>
<meta charset="utf-8">
<title>Under the Willow Tree — eBook Cover</title>
<link rel="stylesheet" href="https://fonts.googleapis.com/css2?family=Bebas+Neue&display=swap">
<style>
  :root {
    --backdrop: #d2d4d6;
    --cover-pink: #e4a0b1;
    --maroon: #5c262c;
    --white: #ffffff;
    --photo-dark: #1f1b1c;
    --photo-mid: #4a3430;
  }
  html, body {
    margin: 0;
    padding: 0;
    width: 1117px;
    height: 1200px;
    overflow: hidden;
    background: var(--backdrop);
  }
  .stage {
    position: relative;
    width: 1117px;
    height: 1200px;
  }
  .cover {
    position: absolute;
    left: 185px;
    top: 40px;
    width: 746px;
    height: 1120px;
    display: block;
  }
  .cover text {
    font-family: 'Bebas Neue', 'Oswald', sans-serif;
  }
  .title-white { fill: var(--white); }
  .title-maroon { fill: var(--maroon); }
  .rule-white { fill: var(--white); }
  .rule-maroon { fill: var(--maroon); }
  .cover-bg { fill: var(--cover-pink); }
  .author-band { fill: var(--maroon); }
</style>
</head>
<body>
<main class="stage">
  <svg class="cover" viewBox="0 0 746 1120" xmlns="http://www.w3.org/2000/svg" aria-label="eBook cover: Under the Willow Tree by KT Dorran">
    <defs>
      <linearGradient id="portraitTone" x1="0" y1="0" x2="0" y2="1">
        <stop offset="0" stop-color="var(--photo-mid)"/>
        <stop offset="0.3" stop-color="var(--photo-dark)"/>
        <stop offset="1" stop-color="var(--photo-dark)"/>
      </linearGradient>
    </defs>

    <rect class="cover-bg" x="0" y="0" width="746" height="1120"/>

    <!-- Portrait area, set behind the headline so the title stays legible -->
    <rect x="362" y="470" width="368" height="568" rx="40" fill="url(#portraitTone)" role="img" aria-label="Portrait photo of the author, smiling and waving, dressed in black"/>

    <!-- Title, first line -->
    <text class="title-white" x="46" y="170" font-size="174" textLength="657" lengthAdjust="spacingAndGlyphs">UNDER THE</text>

    <!-- Connector word with tapered rules -->
    <polygon class="rule-white" points="48,210 318,206 318,214"/>
    <text class="title-white" x="371" y="223" font-size="36" text-anchor="middle">WILLOW</text>
    <polygon class="rule-white" points="424,206 700,210 424,214"/>

    <!-- Headline word -->
    <text class="title-white" x="48" y="548" font-size="437" textLength="652" lengthAdjust="spacingAndGlyphs">TREE</text>

    <!-- Subtitle -->
    <text class="title-maroon" x="46" y="749" font-size="200" textLength="296" lengthAdjust="spacingAndGlyphs">WHERE</text>
    <text class="title-maroon" x="46" y="837" font-size="97" textLength="286" lengthAdjust="spacingAndGlyphs">I FOUND</text>

    <polygon class="rule-maroon" points="48,861 160,859 160,863"/>
    <text class="title-maroon" x="183" y="871" font-size="24" text-anchor="middle">MY</text>
    <polygon class="rule-maroon" points="206,859 316,861 206,863"/>

    <text class="title-maroon" x="47" y="916" font-size="49" textLength="274" lengthAdjust="spacingAndGlyphs">QUIET STRENGTH</text>

    <polygon class="rule-maroon" points="48,933 158,931 158,935"/>
    <text class="title-maroon" x="180" y="941" font-size="21" text-anchor="middle">AND</text>
    <polygon class="rule-maroon" points="202,931 315,933 202,935"/>

    <text class="title-maroon" x="47" y="996" font-size="50" textLength="276" lengthAdjust="spacingAndGlyphs">WHERE YOU MIGHT TOO</text>

    <!-- Author band -->
    <rect class="author-band" x="0" y="1038" width="746" height="82"/>
    <text class="title-white" x="373" y="1093" font-size="34" text-anchor="middle">BY KT DORRAN</text>
  </svg>
</main>
</body>
</html>
```